Elmrow Management real estate management company needs presentation folder to hand clients

looking for a folder with pockets that represent my real estate management company when i hand to client reports or promotional material. I only do resedential real estate. I want classy and professional - pictures or additioal graphixs are fine

when a client open i will usally insert text and reports about my business
also on the inside flap is usally place for my business card i will upload a picture so the theme can be constant

Target Market(s)

my existing real estate cleints
and i will use when i am soliciting new business

Industry/Entity Type

Real Estate

Font styles to use
Serif

Requirements
Must have
• must have logo
• must give appearance of professionalism and maturity
• have basic company info tel# ,address
• id like viewer to know I manage real estate - focus on residential small to large apartment buildings
• not strip malls, not giganic complexes - im a mid size company
• logo is black but i welcome color as u see fit
Nice to have
• maybe pictures
• my slogan - " we will manage your building like its our own "
• focus on professioanl, safe, trust worthy
• type style should be clear and readable - but im open to sugestions

```html
<!DOCTYPE html>
<html lang="en">
<head>
<meta charset="utf-8">
<title>Elmrow Management – Presentation Folder</title>
<link rel="stylesheet" href="https://fonts.googleapis.com/css2?family=Montserrat:wght@400;500;700&family=Arimo:wght@400;700&display=swap">
<style>
  :root {
    --ink: #0b0b0b;
    --paper: #ffffff;
    --slit: #8a3bb5;
    --photo-light: #e9e9e9;
    --photo-mid: #9a9a9a;
    --photo-dark: #1c1c1c;
  }
  * { margin: 0; padding: 0; box-sizing: border-box; }
  html, body { width: 1200px; height: 1075px; overflow: hidden; background: var(--paper); }
  .folder { position: relative; width: 1200px; height: 1075px; font-family: "Montserrat", sans-serif; color: var(--ink); }
  .folder-shapes { position: absolute; left: 0; top: 0; width: 1200px; height: 1075px; }

  .slogan { position: absolute; left: 725px; top: 118px; width: 327px; color: var(--paper); text-align: center; }
  .slogan-rule { height: 1px; background: var(--paper); opacity: .85; }
  .slogan-lead { font-size: 22px; font-weight: 500; letter-spacing: .5px; line-height: 34px; }
  .slogan-main { font-size: 37px; font-weight: 700; line-height: 40px; margin-top: 3px; letter-spacing: .3px; }
  .slogan-tail { font-size: 29px; font-weight: 500; line-height: 34px; letter-spacing: .3px; }

  .contact { position: absolute; left: 138px; top: 534px; font-size: 13.5px; line-height: 19.5px; color: var(--ink); font-style: normal; }

  .brand-mark { position: absolute; left: 1004px; top: 578px; width: 104px; display: flex; align-items: center; gap: 5px; }
  .brand-mark .dot { width: 9px; height: 9px; background: var(--ink); flex: none; }
  .brand-mark .name { font-size: 11px; font-weight: 700; line-height: 13px; text-transform: uppercase; letter-spacing: .4px; }

  .card { position: absolute; left: 248px; top: 844px; width: 202px; height: 111px; background: var(--paper); border: 1px solid #bdbdbd; font-family: "Arimo", sans-serif; }
  .card-brand { position: absolute; left: 8px; top: 28px; width: 78px; display: flex; align-items: center; gap: 4px; }
  .card-brand .dot { width: 6px; height: 6px; background: var(--ink); flex: none; }
  .card-brand .name { font-family: "Montserrat", sans-serif; font-size: 8.5px; font-weight: 700; line-height: 10px; text-transform: uppercase; }
  .card-divider { position: absolute; left: 91px; top: 25px; width: 1px; height: 48px; background: var(--ink); }
  .card-details { position: absolute; right: 10px; top: 25px; text-align: right; }
  .card-name { font-size: 12.5px; font-weight: 700; line-height: 14px; }
  .card-title { font-size: 5.5px; line-height: 7px; text-transform: uppercase; }
  .card-lines { margin-top: 5px; font-size: 5.8px; line-height: 7.2px; }
  .card-address { font-size: 3.6px; line-height: 5px; text-transform: uppercase; font-weight: 700; }
  .card-footer { position: absolute; left: 10px; right: 10px; top: 88px; border-top: 1px solid #9a9a9a; padding-top: 3px; text-align: center; font-size: 4.2px; font-weight: 700; text-transform: uppercase; }
</style>
</head>
<body>
<main class="folder">
  <svg class="folder-shapes" viewBox="0 0 1440 1290" xmlns="http://www.w3.org/2000/svg">
    <defs>
      <linearGradient id="interior-tone" x1="0" y1="0" x2="1" y2="1">
        <stop offset="0" stop-color="#e9e9e9"/>
        <stop offset=".55" stop-color="#9a9a9a"/>
        <stop offset="1" stop-color="#1c1c1c"/>
      </linearGradient>
    </defs>
    <rect class="cover-band" x="131" y="78" width="1234" height="487" fill="#0b0b0b"/>
    <polygon class="frame-outer" points="745,292 1170,547 1170,852 745,915 368,855 368,558" fill="#ffffff"/>
    <polygon class="frame-band" points="745,306 1160,553 1160,843 745,905 378,846 378,565" fill="#0b0b0b"/>
    <polygon class="frame-gap" points="745,318 1148,559 1148,834 745,893 390,835 390,571" fill="#ffffff"/>
    <polygon class="interior-photo" role="img" aria-label="Black and white photo of a bright residential apartment lobby with tall vases and framed art" points="745,326 1142,563 1142,828 745,884 396,829 396,575" fill="url(#interior-tone)"/>
    <path class="pocket" d="M131 938 H731 V1210 Q731 1222 719 1222 H131 L88 1210 V975 Z" fill="#0b0b0b"/>
    <line class="card-slit" x1="275" y1="1050" x2="330" y2="995" stroke="#8a3bb5" stroke-width="1.2"/>
    <line class="card-slit" x1="505" y1="1142" x2="562" y2="1112" stroke="#8a3bb5" stroke-width="1.2"/>
  </svg>

  <section class="slogan">
    <div class="slogan-rule"></div>
    <p class="slogan-lead">WE WILL MANAGE</p>
    <div class="slogan-rule"></div>
    <p class="slogan-main">YOUR BUILDING</p>
    <p class="slogan-tail">LIKE IT IS OUR OWN</p>
  </section>

  <address class="contact">
    phone: 555-210-4470<br>
    email: dh@elmrow.com<br>
    cell: 555-386-9125
  </address>

  <div class="brand-mark">
    <span class="dot"></span>
    <span class="name">Elmrow Management</span>
  </div>

  <article class="card">
    <div class="card-brand">
      <span class="dot"></span>
      <span class="name">Elmrow Management</span>
    </div>
    <div class="card-divider"></div>
    <div class="card-details">
      <p class="card-name">Daniel Hart</p>
      <p class="card-title">Master Building Manager</p>
      <p class="card-lines">office tel 555-210-4470<br>email dh@elmrow.com<br>cell 555-386-9125</p>
      <p class="card-address">24 Alder Court Suite 210 Brookfield NY 10000</p>
    </div>
    <p class="card-footer">We will manage your building like it is our own</p>
  </article>
</main>
</body>
</html>
```